Zielgruppe
Massage-Velora macht Rücken/ Ganzkörpermassage, Intim/ Körperrasur, verschiedene Wellnessanwendungen ...
Ich suche einen neutralen modernen Flyer für Hotels/ Restaurants/ Designshops wie Tolv/ Mendra ...
Leider ist mein Grafiker Anfang Mai nach Krankheit plötzlich verstorben!
Anbei viele Motive .. vielleicht finde ich hier wieder einen Partner für Anzeigen/ Aufkleber und Flyer!
Herzlichen Dank
Wilfried
Aufgabenstellung
Postkartenformat
Dopp Visitenkarte

```html
<!DOCTYPE html>
<html lang="de">
<head>
<meta charset="utf-8">
<title>Massage-Velora Flyer A6</title>
<link rel="stylesheet" href="https://fonts.googleapis.com/css2?family=Open+Sans:wght@400;600;700;800&display=swap">
<style>
  :root{
    --orange:#ec7a0c;
    --blue:#1ea1db;
    --white:#ffffff;
    --grey-text:#555555;
    --grey-light:#8a8a8a;
    --stage:#33231a;
    --photo-warm-a:#f6dccd;
    --photo-warm-b:#e8b596;
    --body-cream-a:#fff4dc;
    --body-cream-b:#f8cf7a;
  }
  *{margin:0;padding:0;box-sizing:border-box;}
  html,body{width:1200px;height:849px;overflow:hidden;background:var(--stage);}
  body{font-family:"Open Sans",Arial,sans-serif;position:relative;}
  .flyer{position:absolute;top:76px;width:494px;height:696px;overflow:hidden;box-shadow:0 8px 24px rgba(0,0,0,.45);}
  .flyer--left{left:72px;background:linear-gradient(180deg,var(--photo-warm-a),var(--photo-warm-b));}
  .flyer--right{left:634px;background:linear-gradient(180deg,var(--body-cream-a) 40%,var(--body-cream-b));}
  .header-card{position:absolute;left:15px;top:0;width:464px;background:var(--white);box-shadow:0 10px 14px rgba(0,0,0,.22);z-index:3;}
  .flyer--left .header-card{height:226px;}
  .flyer--right .header-card{height:232px;}
  .brand-name{position:absolute;left:18px;top:64px;color:var(--orange);font-weight:700;font-size:29px;line-height:36px;white-space:nowrap;}
  .badge{position:absolute;right:28px;top:32px;width:106px;height:106px;border-radius:50%;background:var(--blue);color:var(--white);text-align:center;display:flex;flex-direction:column;justify-content:center;font-weight:800;line-height:1.05;}
  .badge .big{font-size:19px;}
  .badge .small{font-size:12px;font-weight:600;margin-top:3px;}
  .services{position:absolute;left:0;right:0;top:160px;text-align:center;color:var(--grey-text);font-size:20px;line-height:26px;}
  .tagline{position:absolute;left:0;right:0;top:162px;text-align:center;font-size:19px;line-height:24px;}
  .tagline .line1{color:var(--grey-text);font-weight:600;}
  .tagline .line2{color:var(--grey-light);font-weight:600;}
  .photo{position:absolute;z-index:1;}
  .flyer--left .photo{left:0;top:226px;width:494px;height:340px;background:linear-gradient(135deg,#f3d3c1,#dda07e 60%,#f0cdb9);}
  .flyer--right .photo{left:332px;top:220px;width:162px;height:330px;background:linear-gradient(180deg,#b57a55,#8a5a40 70%,#6d6d6d);border-radius:60px 40px 0 0;}
  .list{position:absolute;left:30px;color:var(--grey-text);font-size:18px;line-height:24px;z-index:2;list-style:none;}
  .list--de{top:262px;}
  .list--en{top:402px;}
  .new-dot{display:inline-block;width:20px;height:20px;border-radius:50%;background:var(--orange);color:var(--white);font-size:8px;font-weight:700;text-align:center;line-height:20px;vertical-align:middle;margin-left:6px;}
  .footer-wave{position:absolute;left:0;top:470px;width:494px;height:226px;z-index:4;}
  .call-now{position:absolute;right:40px;top:500px;width:64px;height:64px;border-radius:50%;background:var(--orange);border:3px solid var(--white);color:var(--white);font-weight:800;font-size:16px;line-height:16px;text-align:center;display:flex;align-items:center;justify-content:center;z-index:5;}
  .contact{position:absolute;left:26px;top:572px;color:var(--white);font-size:14px;line-height:19px;font-style:normal;z-index:5;}
  .phone{position:absolute;right:22px;top:576px;color:var(--white);text-align:right;z-index:5;}
  .phone .number{font-weight:800;font-size:26px;line-height:30px;}
  .phone .note{font-size:14px;line-height:18px;}
  .website{position:absolute;left:0;right:0;top:636px;text-align:center;color:var(--white);font-weight:800;font-size:33px;line-height:40px;letter-spacing:-0.5px;z-index:5;}
</style>
</head>
<body>

<section class="flyer flyer--left">
  <header class="header-card">
    <div class="brand-name">Massage-Velora</div>
    <div class="badge"><span class="big">KEIN</span><span class="big">RUHETAG</span><span class="small">OPEN DAILY</span></div>
    <p class="services">Ganzkörper · Rücken · Po-Relax · Intimrasur<br>Fußmassage · Bondagemassage</p>
  </header>
  <div class="photo" role="img" aria-label="Foto: entspannter Mann liegt lächelnd auf der Massageliege"></div>
  <svg class="footer-wave" viewBox="0 0 494 226" preserveAspectRatio="none" aria-hidden="true">
    <path d="M0 70 Q240 130 494 20 L494 226 L0 226 Z" fill="var(--orange)"/>
    <path d="M0 70 Q240 130 494 20" fill="none" stroke="var(--white)" stroke-width="3"/>
  </svg>
  <div class="call-now">CALL<br>NOW</div>
  <address class="contact">Studio Lindenweg 14 (4. OG)<br>80469 München<br>info@massage-velora.ch</address>
  <div class="phone"><div class="number">0175-482 19 63</div><div class="note">Termin nach Vereinbarung</div></div>
  <div class="website">MASSAGE-VELORA.COM</div>
</section>

<section class="flyer flyer--right">
  <header class="header-card">
    <div class="brand-name">Massage-Velora</div>
    <div class="badge"><span class="big">STUDIO</span><span class="big">OUTCALL</span><span class="small">HAUS &amp; HOTEL</span></div>
    <p class="tagline"><span class="line1">REALX AND ENJOY YOUR LIFE</span><br><span class="line2">MASSAGE SERVICE BIS 24.00</span></p>
  </header>
  <div class="photo" role="img" aria-label="Foto: muskulöser Mann von hinten, Hand im Nacken"></div>
  <ul class="list list--de">
    <li>Rücken- &amp; Ganzkörpermassage</li>
    <li>Po Relax Massage, Tantra</li>
    <li>Bondage (Fessel) Massage<span class="new-dot">NEU</span></li>
    <li>Streichen &amp; Berührung</li>
    <li>Intim- &amp; Körperrasur</li>
  </ul>
  <ul class="list list--en">
    <li>full body massage, swedish</li>
    <li>buttockmassage, tantric</li>
    <li>bondage massage<span class="new-dot">NEW</span></li>
    <li>gentle touch, foam massage</li>
    <li>intimate- &amp; body shaving</li>
  </ul>
  <svg class="footer-wave" viewBox="0 0 494 226" preserveAspectRatio="none" aria-hidden="true">
    <path d="M0 70 Q240 130 494 20 L494 226 L0 226 Z" fill="var(--orange)"/>
    <path d="M0 70 Q240 130 494 20" fill="none" stroke="var(--white)" stroke-width="3"/>
  </svg>
  <div class="call-now">CALL<br>NOW</div>
  <address class="contact">Studio Lindenweg 14 (4. OG)<br>80469 München<br>info@massage-velora.ch</address>
  <div class="phone"><div class="number">0175-482 19 63</div><div class="note">Termin nach Vereinbarung</div></div>
  <div class="website">MASSAGE-VELORA.COM</div>
</section>

</body>
</html>
```